Business Card Design Project

Please create a custom business card for Plume analytics. The logo is attached to this brief.

Address :
CEO : Baptiste Lorand
Mobile : +33641927508
14 rue Véronèse
75013 Paris
France

Reason: Sorry wrong logo. I will update asap

Hi, Sorry, I post the wrong file. I just update the correct logo. If you can integrate some charts as background it will be nice

Hi Everybody Please make it beautifull, clean, soft like pebble designs does to create their product. I want somewhere to show in a beautifull way some datavisualization charts. Not to much, but try to find a way to design it beautifull with less. Get inspire by datavisualization : http://www.morvelkit.com/48207-clean-vector-infographic-and-data-visualization-design-elements-03/

Target Market(s)

B to B
Customers are accountant, CPA, finance departement

Industry/Entity Type

Business

Font styles to use
Sans Serif

Requirements
Must have
• I want to give a clear message about what we do. We do dashboards, we create beautifull charts
Nice to have
• displays charts icons to let people know tha we do charts

```html
<!DOCTYPE html>
<html lang="en">
<head>
<meta charset="utf-8">
<title>Plume analytics — business card</title>
<link rel="stylesheet" href="https://fonts.googleapis.com/css2?family=Michroma&family=Varela+Round&family=Open+Sans:wght@600&display=swap">
<style>
  :root {
    --backdrop: #2b2b2b;
    --card-black: #0c0c0c;
    --band-light: #f2f2f2;
    --band-mid: #c9c9c9;
    --band-dark: #9d9d9d;
    --brand-blue: #1ea6e4;
    --ink-dark: #2e2e2e;
    --ink-grey: #5a5a5a;
    --back-light: #d5dadb;
    --back-mid: #b4bbbd;
    --back-dark: #9aa2a5;
    --chart-ink: #ffffff;
  }
  * { box-sizing: border-box; margin: 0; padding: 0; }
  html, body { width: 1200px; height: 900px; overflow: hidden; }
  body { background: var(--backdrop); position: relative; }

  .card {
    position: absolute;
    width: 665px;
    height: 380px;
    border-radius: 0 110px 0 110px;
    overflow: hidden;
    box-shadow: 0 10px 30px rgba(0,0,0,.45);
  }

  /* Front */
  .card--front { left: 80px; top: 50px; background: var(--card-black); }
  .front__brand {
    position: absolute; left: 44px; top: 46px;
    display: flex; align-items: center; gap: 12px;
  }
  .brand__square { width: 30px; height: 30px; background: var(--brand-blue); flex: none; }
  .brand__name {
    font-family: "Varela Round", sans-serif;
    color: var(--brand-blue);
    font-size: 28px; letter-spacing: .2px; line-height: 1;
    white-space: nowrap;
  }
  .front__band {
    position: absolute; left: 0; right: 0; top: 110px; height: 150px;
    background: linear-gradient(90deg, var(--band-dark) 0%, var(--band-mid) 20%, var(--band-light) 55%, var(--band-mid) 85%, var(--band-dark) 100%);
  }
  .person { position: absolute; left: 40px; top: 62px; }
  .person__name {
    font-family: "Michroma", sans-serif;
    font-size: 21px; letter-spacing: 2px; text-transform: uppercase;
    white-space: nowrap;
  }
  .person__first { color: var(--brand-blue); }
  .person__last { color: var(--ink-dark); }
  .person__role {
    font-family: "Michroma", sans-serif; font-size: 10px; color: var(--ink-grey);
    text-align: right; margin-top: 4px; letter-spacing: 1px;
  }
  .front__divider {
    position: absolute; left: 370px; top: 22px; width: 2px; height: 108px; background: #1a1a1a;
  }
  .contact {
    position: absolute; left: 392px; top: 22px;
    font-family: "Michroma", sans-serif; font-size: 12px; color: #1c1c1c;
    letter-spacing: 1.4px; text-transform: uppercase; line-height: 1.5;
  }
  .contact__row { display: flex; gap: 12px; align-items: flex-start; margin-bottom: 10px; }
  .contact__icon { width: 16px; height: 16px; flex: none; margin-top: 2px; }

  /* Back */
  .card--back {
    left: 455px; top: 470px;
    background: radial-gradient(ellipse at 62% 55%, var(--back-light) 0%, var(--back-mid) 60%, var(--back-dark) 100%);
  }
  .back__chart { position: absolute; inset: 0; }
  .back__brand {
    position: absolute; left: 150px; top: 150px;
    display: flex; align-items: center; gap: 16px;
  }
  .back__brand .brand__square { width: 52px; height: 52px; }
  .back__brand .brand__name { font-size: 44px; }
  .back__wordmark { display: flex; flex-direction: column; align-items: flex-end; }
  .back__tagline {
    margin-top: 6px;
    font-family: "Open Sans", sans-serif; font-weight: 600;
    font-size: 12px; color: var(--ink-grey);
  }
</style>
</head>
<body>

<section class="card card--front">
  <div class="front__brand">
    <span class="brand__square"></span>
    <span class="brand__name">Plume analytics</span>
  </div>
  <div class="front__band">
    <div class="person">
      <p class="person__name"><span class="person__first">Baptiste</span> <span class="person__last">Lorand</span></p>
      <p class="person__role">C.E.O</p>
    </div>
    <div class="front__divider"></div>
    <div class="contact">
      <div class="contact__row">
        <svg class="contact__icon" viewBox="0 0 16 16" aria-hidden="true">
          <path d="M1 6c0-2 3-3 7-3s7 1 7 3v1h-3V5.5H4V7H1z" fill="#1c1c1c"/>
          <rect x="3" y="8" width="10" height="6" rx="1" fill="#1c1c1c"/>
          <circle cx="8" cy="11" r="1.6" fill="#dcdcdc"/>
        </svg>
        <span>+33641927508</span>
      </div>
      <div class="contact__row">
        <svg class="contact__icon" viewBox="0 0 16 16" aria-hidden="true">
          <path d="M8 1a5 5 0 0 0-5 5c0 4 5 9 5 9s5-5 5-9a5 5 0 0 0-5-5z" fill="#1c1c1c"/>
          <circle cx="8" cy="6" r="1.8" fill="#dcdcdc"/>
        </svg>
        <span>14 rue Véronèse<br>75013 Paris<br>France</span>
      </div>
    </div>
  </div>
</section>

<section class="card card--back">
  <svg class="back__chart" viewBox="0 0 665 380" aria-hidden="true">
    <g class="chart__grid" stroke="var(--chart-ink)" stroke-opacity=".22" stroke-width="1">
      <line x1="40" y1="330" x2="625" y2="330"/>
      <line x1="40" y1="270" x2="625" y2="270" stroke-dasharray="3 5"/>
      <line x1="40" y1="210" x2="625" y2="210" stroke-dasharray="3 5"/>
      <line x1="40" y1="150" x2="625" y2="150" stroke-dasharray="3 5"/>
      <line x1="40" y1="90" x2="625" y2="90" stroke-dasharray="3 5"/>
    </g>
    <g class="chart__bars" fill="var(--chart-ink)" fill-opacity=".2">
      <rect x="70" y="290" width="34" height="40"/>
      <rect x="130" y="262" width="34" height="68"/>
      <rect x="190" y="276" width="34" height="54"/>
      <rect x="250" y="240" width="34" height="90"/>
      <rect x="310" y="254" width="34" height="76"/>
      <rect x="370" y="222" width="34" height="108"/>
      <rect x="430" y="236" width="34" height="94"/>
      <rect x="490" y="200" width="34" height="130"/>
      <rect x="550" y="176" width="34" height="154"/>
    </g>
    <g class="chart__trend" fill="none" stroke="var(--chart-ink)" stroke-opacity=".45" stroke-width="1.6">
      <polyline points="87,250 147,222 207,232 267,190 327,204 387,160 447,172 507,128 567,96"/>
    </g>
    <g class="chart__points" fill="var(--chart-ink)" fill-opacity=".55">
      <circle cx="87" cy="250" r="3"/><circle cx="147" cy="222" r="3"/><circle cx="207" cy="232" r="3"/>
      <circle cx="267" cy="190" r="3"/><circle cx="327" cy="204" r="3"/><circle cx="387" cy="160" r="3"/>
      <circle cx="447" cy="172" r="3"/><circle cx="507" cy="128" r="3"/><circle cx="567" cy="96" r="3"/>
    </g>
  </svg>
  <div class="back__brand">
    <span class="brand__square"></span>
    <div class="back__wordmark">
      <span class="brand__name">Plume analytics</span>
      <p class="back__tagline">Visualize your data</p>
    </div>
  </div>
</section>

</body>
</html>
```